Small consulting business needs a website designed to highlight value and four offerings

My company is a dynamic consulting firm with four Core Offerings: Learning & Evaluation, Program Management, Facilitation & Coaching; Implementation & Transformation. Our mission is to facilitate organizational change and transformation, and to make space for creativity, joy, belonging, and trust. If done successfully, we grow to better understand ourselves, each other, and the work we do together.

I'd like the website to give a feeling of confidence and clarity. I want the colors to match or compliment my logo. I want to have three tabs - Our Clients, Our Services, and Government.

See attached Word document for additional content. My current website is www.BrightHarborGroup.com.

Some websites I'm inspired by:
https://www.quillmeadowworks.com
https://www.verolandpartners.com
https://tqvb.org

Some websites of people/groups in my field that I find uninspiring:
http://denisehollick.com
https://www.marrowfen.org

Target Market(s)

State and local government agencies, health tech, and corporate HR departments

Industry/Entity Type

public health, aging, government, health tech

Coding

Coded - Design and coding required

Number of Pages Required

4 page

Font styles to use
Other font styles liked:
• Calibri and Merriweather

Colors
0054AA
0677BA
7BADD7
CADEEF
E8F1F8
00AB8E
00BBA5
67D7C9
C6EFE9
E9F9F6
FFC000
F8CF3A
FAE287
FDF2CF
FEFAEE
F0912C
F2A743
F7CA91
FBE8D2
FDF5EE

Requirements
Must have
• Attached logo and content, water colors few, and photos.
Nice to have
• Real pictures, which I can provide to the chosen designer
Should not have
• AI generated characters or cartoons.

```html
<!DOCTYPE html>
<html lang="en">
<head>
<meta charset="UTF-8">
<title>Bright Harbor Group</title>
<link href="https://fonts.googleapis.com/css2?family=Inter:wght@400;500&family=Newsreader:opsz,wght@6..72,400&display=swap" rel="stylesheet">
<style>
  :root {
    --ink: #111114;
    --dark: #222226;
    --muted: #b9b9bd;
    --soft: #7d7d82;
    --sun: #f2d98a;
    --gold: #f8cf3a;
    --teal: #1f7a6a;
    --leaf: #9fb84a;
    --white: #ffffff;
  }
  * { box-sizing: border-box; margin: 0; padding: 0; }
  html, body { width: 1200px; height: 731px; overflow: hidden; background: var(--white); }
  body { position: relative; font-family: "Inter", sans-serif; color: var(--ink); }

  .site-header { position: absolute; inset: 0 0 auto 0; height: 95px; }
  .brand { position: absolute; left: 48px; top: 26px; display: flex; align-items: center; gap: 8px; }
  .brand-dot { width: 30px; height: 30px; border-radius: 50%; background: var(--gold); }
  .brand-name { font-family: "Newsreader", serif; font-size: 15px; line-height: 14px; width: 90px; color: var(--ink); }
  .main-nav { position: absolute; left: 283px; top: 37px; display: flex; gap: 17px; }
  .main-nav a { font-size: 16px; color: var(--ink); text-decoration: none; line-height: 20px; }
  .btn { display: inline-flex; align-items: center; justify-content: center; gap: 8px; height: 44px; border-radius: 6px; font-size: 16px; font-weight: 500; text-decoration: none; }
  .btn svg { width: 15px; height: 15px; }
  .header-cta { position: absolute; left: 1009px; top: 25px; width: 143px; background: var(--dark); color: var(--white); }

  .hero-copy { position: absolute; left: 96px; top: 170px; width: 470px; }
  .hero-badge { display: inline-block; height: 32px; line-height: 32px; padding: 0 14px; border-radius: 8px; background: var(--dark); color: var(--white); font-size: 14px; }
  .hero-title { margin-top: 20px; font-family: "Newsreader", serif; font-weight: 400; font-size: 46px; line-height: 48px; letter-spacing: -0.5px; }
  .hero-lead { margin-top: 22px; width: 455px; font-size: 15.5px; line-height: 22px; color: var(--muted); }
  .hero-actions { margin-top: 32px; display: flex; gap: 12px; }
  .btn-primary { width: 144px; background: var(--sun); color: var(--ink); }
  .btn-outline { width: 143px; border: 2px solid var(--dark); color: var(--ink); }
  .hero-note { margin-top: 26px; font-size: 14px; color: var(--soft); }

  .hero-art { position: absolute; left: 675px; top: 232px; width: 352px; height: 352px; border-radius: 50%;
    background: radial-gradient(circle at 30% 65%, #f5b726 0%, #f2c94c 30%, transparent 55%),
                radial-gradient(circle at 72% 35%, #3f9c85 0%, #7fc2a6 35%, transparent 60%),
                linear-gradient(135deg, #b8b83e 0%, #f3bb2e 45%, #4d9c82 60%, #1f6e62 100%);
    border: 8px solid #1c5a55; }
</style>
</head>
<body>
  <header class="site-header">
    <div class="brand">
      <span class="brand-dot"></span>
      <span class="brand-name">Bright Harbor Group</span>
    </div>
    <nav class="main-nav">
      <a href="#">Home</a>
      <a href="#">About Us</a>
      <a href="#">Case Studies</a>
      <a href="#">Our Clients</a>
      <a href="#">Our Services</a>
      <a href="#">Government</a>
      <a href="#">Contact</a>
    </nav>
    <a class="btn header-cta" href="#">
      <svg viewBox="0 0 24 24" fill="none" stroke="currentColor" stroke-width="2" stroke-linecap="round" stroke-linejoin="round"><path d="M22 16.9v3a2 2 0 0 1-2.2 2 19.8 19.8 0 0 1-8.6-3.1 19.5 19.5 0 0 1-6-6A19.8 19.8 0 0 1 2.1 4.2 2 2 0 0 1 4.1 2h3a2 2 0 0 1 2 1.7c.1.9.4 1.8.7 2.7a2 2 0 0 1-.5 2.1L8 9.8a16 16 0 0 0 6 6l1.3-1.3a2 2 0 0 1 2.1-.4c.9.3 1.8.6 2.7.7a2 2 0 0 1 1.7 2z"/></svg>
      Contact Us
    </a>
  </header>

  <main>
    <section class="hero-copy">
      <span class="hero-badge">Partnerships for sustained progress</span>
      <h1 class="hero-title">A Seat at the Table for Collaboration, Learning, and Meaningful Change.</h1>
      <p class="hero-lead">Bright Harbor Group is a dynamic consulting firm with four Core Offerings: Learning &amp; Evaluation, Program Management, Facilitation &amp; Coaching - Implementation &amp; Transformation.</p>
      <div class="hero-actions">
        <a class="btn btn-primary" href="#">Learn More
          <svg viewBox="0 0 24 24" fill="none" stroke="currentColor" stroke-width="2" stroke-linecap="round" stroke-linejoin="round"><path d="M5 12h14M13 6l6 6-6 6"/></svg>
        </a>
        <a class="btn btn-outline" href="#">
          <svg viewBox="0 0 24 24" fill="none" stroke="currentColor" stroke-width="2" stroke-linecap="round" stroke-linejoin="round"><path d="M22 16.9v3a2 2 0 0 1-2.2 2 19.8 19.8 0 0 1-8.6-3.1 19.5 19.5 0 0 1-6-6A19.8 19.8 0 0 1 2.1 4.2 2 2 0 0 1 4.1 2h3a2 2 0 0 1 2 1.7c.1.9.4 1.8.7 2.7a2 2 0 0 1-.5 2.1L8 9.8a16 16 0 0 0 6 6l1.3-1.3a2 2 0 0 1 2.1-.4c.9.3 1.8.6 2.7.7a2 2 0 0 1 1.7 2z"/></svg>
          Contact Us
        </a>
      </div>
      <p class="hero-note">Driving measurable, human-centric outcomes</p>
    </section>

    <div class="hero-art" role="img" aria-label="Watercolor illustration of four interlocking puzzle pieces in yellow and green forming a circle"></div>
  </main>
</body>
</html>
```